International Internship Provider Needs Catalogue Layout & Design

We need a catalogue/booklet created to send out to university students and study abroad offices. We provide international internships to university students and young professionals in a range of fields in nine cities across the globe. Our program includes guaranteed internship, accommodation, social events, and support from staff. We would like to provide a clean, glossy, and picture-heavy publication to promote our program and website. We'd like to use captivating colors and the final product should convey what our program does and express the fun of living abroad with the professionalism of an internship.

Reason: We've increased the budget by $100, and we understand the project is a large undertaking. Thank you!

We would like each location to be two pages with large images of that location as well as all of the copy in the word document attached. Attached on the images is as an example of another catalogue we liked the style of for you to look at it. If you need any more details or would like me to break up the copy into sections please do not hesitate to ask. thank you!  

I've added new file of content that includes everything in the previous file plus more information, but on separate pages to help make it clear what information goes together. The location should still be a two-page spread that includes a large location image. We would like to have a quote from a student on each of those pages as well. 

I've added more photos for the location pages labeled by the location (ex: London_girls). I've also added some photos for Project Kelvo and new content. Please contact me with any questions. 

Reason: We realized we've asked for a few more edits from designers and we appreciate the time it takes to be make these constant edits. Thank you!

University students and recent college graduates. Usually the target market is between 21-23 years of age, and most students who travel abroad are female.

University

• It must be at least 10 pages and use the logo I've attached. Please be sure to look at the word document that is full of content that will be used in the project. Large photos of the locations are ideal as well 2 pages for each location.
• I have loads of photos I can give to you to use in the document, but you can use placeholders for now or some of the photos I've attached. I've also included a document full of copy that will need to be in the document just to give you an idea of where things will be displayed.

```html
<!DOCTYPE html>
<html lang="en">
<head>
<meta charset="utf-8">
<title>Wayfarer Internships – Catalogue Spread</title>
<link href="https://fonts.googleapis.com/css2?family=Open+Sans:wght@400;600;700;800&family=Oswald:wght@500;600&display=swap" rel="stylesheet">
<style>
  :root {
    --stage: #d6d6d6;
    --navy: #1d3f72;
    --navy-deep: #163463;
    --green: #8cc63f;
    --green-bright: #93cc2c;
    --sky: #66c2ee;
    --sky-pale: #d4eefb;
    --lime: #c9e13a;
    --white: #ffffff;
    --ink-soft: #eef6e4;
  }
  * { box-sizing: border-box; margin: 0; padding: 0; }
  html, body { width: 1200px; height: 773px; overflow: hidden; }
  body {
    background: var(--stage);
    font-family: "Open Sans", Arial, sans-serif;
    position: relative;
  }
  .spread {
    position: absolute; left: 100px; top: 36px;
    width: 1000px; height: 700px;
    display: flex;
    box-shadow: 0 6px 18px rgba(0,0,0,.18);
  }
  .page { position: relative; width: 500px; height: 700px; overflow: hidden; }

  /* ---------- Left page ---------- */
  .page--why {
    background: linear-gradient(to bottom,
      var(--sky) 0%, var(--sky-pale) 20%, #f6fbfe 31%,
      #c4e48a 36%, var(--green-bright) 41%, var(--green) 100%);
  }
  .brand {
    position: absolute; left: 28px; top: 38px;
    display: flex; align-items: center; gap: 10px;
  }
  .brand__mark {
    width: 38px; height: 38px; border-radius: 50%;
    background: var(--white);
  }
  .brand__name {
    color: var(--white); font-weight: 700; font-size: 17px;
    letter-spacing: .06em; text-transform: uppercase; line-height: 1.05;
  }
  .landmark-collage {
    position: absolute; right: 22px; top: 18px;
    width: 250px; height: 165px;
    background: linear-gradient(160deg, #bfe3f6 0%, #d9c9a0 45%, #b86a3a 75%, #e9b652 100%);
    border-radius: 4px;
  }
  .why__title {
    position: absolute; left: 28px; top: 196px;
    color: var(--navy); font-weight: 700; font-size: 20px;
  }
  .columns {
    position: absolute; left: 24px; top: 232px; right: 20px;
    display: grid; grid-template-columns: 258px 1fr; column-gap: 20px;
  }
  .feature { margin-bottom: 14px; }
  .feature__head {
    display: flex; align-items: center; gap: 7px;
    color: var(--navy); font-weight: 800; font-size: 13.5px; margin-bottom: 4px;
  }
  .tick { flex: none; width: 17px; height: 17px; }
  .feature p {
    color: var(--white); font-size: 9.6px; line-height: 1.42; padding-left: 24px;
  }
  .feature--wide { grid-column: 1 / -1; }
  .locations-note {
    color: var(--navy); font-size: 8.5px; line-height: 1.45; padding-left: 24px; margin-top: 6px;
  }
  .locations-note strong { display: block; }
  .folio {
    position: absolute; left: 0; bottom: 0; width: 100%; height: 26px;
    display: flex; align-items: center; gap: 8px;
  }
  .folio__num {
    background: var(--navy); color: var(--white);
    font-size: 10px; font-weight: 700;
    width: 34px; height: 100%; display: flex; align-items: center; justify-content: flex-end; padding-right: 6px;
  }
  .folio__name {
    color: var(--white); font-size: 10px; font-weight: 600;
    letter-spacing: .06em; text-transform: uppercase;
  }

  /* ---------- Right page ---------- */
  .page--city { background: var(--navy); }
  .photo-stack {
    position: absolute; left: 0; top: 0; width: 150px; height: 330px;
    display: flex; flex-direction: column;
  }
  .photo { flex: 1; }
  .photo--friends { background: linear-gradient(150deg, #3a2a2a 0%, #b24a3a 50%, #e3b08c 100%); }
  .photo--park { background: linear-gradient(170deg, #8fc4ea 0%, #d8cfae 55%, #6f8a4a 100%); }
  .snapshot {
    position: absolute; left: 168px; top: 20px; right: 22px;
    color: var(--white);
  }
  .snapshot__title-row { display: flex; align-items: flex-end; gap: 8px; margin-bottom: 8px; }
  .landmark-icon {
    width: 26px; height: 36px;
    background: linear-gradient(to top, #b5742f, #e3b35b);
    border-radius: 3px 3px 0 0;
  }
  .city-name {
    font-family: "Oswald", "Arial Narrow", sans-serif;
    color: var(--lime); font-weight: 600; font-size: 27px; letter-spacing: .02em; line-height: 1;
  }
  .sub-head {
    color: var(--lime); font-weight: 700; font-size: 12.5px; margin: 6px 0 3px;
  }
  .snapshot p { font-size: 9.2px; line-height: 1.42; }
  .snapshot ul { list-style: none; font-size: 9.2px; line-height: 1.45; }
  .snapshot li::before { content: "•"; color: var(--white); margin-right: 6px; }
  .snapshot ul.terms { margin: 6px 0 2px; }
  .city-view {
    position: absolute; left: 0; bottom: 0; width: 100%; height: 370px;
    background: linear-gradient(115deg, #d9cfbd 0%, #c8b79b 35%, #e6e0d2 55%, #7fbfb5 72%, #2fb3b0 86%, #27a8b3 100%);
  }
</style>
</head>
<body>
  <main class="spread">
    <!-- Left page: why choose -->
    <section class="page page--why">
      <div class="brand">
        <span class="brand__mark"></span>
        <span class="brand__name">Wayfarer<br>Internships</span>
      </div>
      <div class="landmark-collage" role="img" aria-label="Collage of world landmarks with a suitcase and passport"></div>

      <h1 class="why__title">Why Choose Wayfarer Internships</h1>

      <div class="columns">
        <div>
          <article class="feature">
            <h2 class="feature__head"><svg class="tick" viewBox="0 0 20 20"><circle cx="10" cy="10" r="10" fill="#1d3f72"/><path d="M5.5 10.5l3 3 6-6.5" fill="none" stroke="#fff" stroke-width="2.2" stroke-linecap="round" stroke-linejoin="round"/></svg>Guaranteed Internships</h2>
            <p>If accepted into the program, we guarantee your internship placement. We work with your goals and skills to secure a role that fits your field, so you can focus on growing professionally from day one.</p>
          </article>
          <article class="feature">
            <h2 class="feature__head"><svg class="tick" viewBox="0 0 20 20"><circle cx="10" cy="10" r="10" fill="#1d3f72"/><path d="M5.5 10.5l3 3 6-6.5" fill="none" stroke="#fff" stroke-width="2.2" stroke-linecap="round" stroke-linejoin="round"/></svg>Extensive Career Development</h2>
            <p>All of our interns take part in career workshops before, during and after the program. From resume reviews to networking sessions, our team helps you turn global experience into a real advantage on your career path.</p>
          </article>
          <article class="feature">
            <h2 class="feature__head"><svg class="tick" viewBox="0 0 20 20"><circle cx="10" cy="10" r="10" fill="#1d3f72"/><path d="M5.5 10.5l3 3 6-6.5" fill="none" stroke="#fff" stroke-width="2.2" stroke-linecap="round" stroke-linejoin="round"/></svg>Individual Support</h2>
            <p>From the first phone call to the last day abroad, you work with one dedicated advisor. Our local coordinators are available around the clock and can answer questions, solve problems and act as your emergency contact.</p>
          </article>
        </div>
        <div>
          <article class="feature">
            <h2 class="feature__head"><svg class="tick" viewBox="0 0 20 20"><circle cx="10" cy="10" r="10" fill="#1d3f72"/><path d="M5.5 10.5l3 3 6-6.5" fill="none" stroke="#fff" stroke-width="2.2" stroke-linecap="round" stroke-linejoin="round"/></svg>Local Staff</h2>
            <p>Our staff live and work in each city, so they know the best neighborhoods, cafes and routes to work. They welcome you on arrival and stay close throughout your stay.</p>
          </article>
          <article class="feature">
            <h2 class="feature__head"><svg class="tick" viewBox="0 0 20 20"><circle cx="10" cy="10" r="10" fill="#1d3f72"/><path d="M5.5 10.5l3 3 6-6.5" fill="none" stroke="#fff" stroke-width="2.2" stroke-linecap="round" stroke-linejoin="round"/></svg>University Partnerships</h2>
            <p>We partner with universities across the country to offer academic credit options. Many schools recognize our program, so talk with your study abroad office about how your internship can count toward your degree.</p>
            <p class="locations-note"><strong>Locations:</strong>*Note: These should each be their own page in a page spread with pictures.</p>
          </article>
        </div>
        <article class="feature feature--wide">
          <h2 class="feature__head"><svg class="tick" viewBox="0 0 20 20"><circle cx="10" cy="10" r="10" fill="#1d3f72"/><path d="M5.5 10.5l3 3 6-6.5" fill="none" stroke="#fff" stroke-width="2.2" stroke-linecap="round" stroke-linejoin="round"/></svg>Unique Social Events &amp; Excursions</h2>
          <p>An internship is hard work, but we have planned several city-specific events and excursions to help you meet other interns and explore your new home. Past groups have taken cooking classes in Barcelona, toured castles near London and watched sunsets over Sydney.</p>
        </article>
      </div>

      <footer class="folio">
        <span class="folio__num">3</span>
        <span class="folio__name">Wayfarer Internships</span>
      </footer>
    </section>

    <!-- Right page: Barcelona -->
    <section class="page page--city">
      <div class="photo-stack">
        <div class="photo photo--friends" role="img" aria-label="Group of smiling interns posing together"></div>
        <div class="photo photo--park" role="img" aria-label="Interns relaxing on a mosaic bench in a city park"></div>
      </div>

      <div class="snapshot">
        <div class="snapshot__title-row">
          <span class="landmark-icon" role="img" aria-label="Illustration of a cathedral spire"></span>
          <h1 class="city-name">BARCELONA, SPAIN</h1>
        </div>
        <h2 class="sub-head">Program Snapshot</h2>
        <p>Spend your summer or semester living in the Mediterranean city of Barcelona. Intern with local firms by day, then explore beaches, markets and the famous architecture by night. Placements run in English across many fields.</p>
        <ul class="terms">
          <li>Spring and Fall: 12 week programs</li>
          <li>Summer: 8 and 10 week programs</li>
        </ul>
        <h2 class="sub-head">Inclusions</h2>
        <ul>
          <li>Guaranteed internship placement</li>
          <li>Furnished shared apartment</li>
          <li>Airport pickup on arrival</li>
          <li>Local phone and SIM card</li>
          <li>Welcome dinner and city tour</li>
          <li>Weekly social events</li>
          <li>Day trip to Montserrat</li>
          <li>Career development workshops</li>
          <li>24/7 on-site support</li>
          <li>Medical insurance</li>
        </ul>
      </div>

      <div class="city-view" role="img" aria-label="Aerial view of the Barcelona waterfront and city blocks beside turquoise sea"></div>
    </section>
  </main>
</body>
</html>
```